Letterhead, business card and email signature design

I have a new company and I would like a professional letterhead, business card and email signature designed. Id like the business card to have room for a photo of the bearer. I'd also like the template to be editable so we can adapt for future members of staff etc.

```html
<!DOCTYPE html>
<html lang="en">
<head>
<meta charset="utf-8">
<title>Nimbus Systems – Business Card Front</title>
<link rel="stylesheet" href="https://fonts.googleapis.com/css2?family=Michroma&display=swap">
<style>
  :root {
    --navy: #0f2868;
    --magenta: #a0077a;
    --paper-light: #fbfcfc;
    --paper-edge: #e4e9eb;
    --gap-white: #ffffff;
    --brand-font: "Michroma", sans-serif;
  }
  * { margin: 0; padding: 0; box-sizing: border-box; }
  html, body {
    width: 1200px;
    height: 720px;
    overflow: hidden;
    background: var(--paper-edge);
  }
  .card-front {
    position: relative;
    width: 1200px;
    height: 720px;
    overflow: hidden;
    background: radial-gradient(ellipse 70% 70% at 50% 45%, var(--paper-light) 0%, #f2f5f6 60%, var(--paper-edge) 100%);
  }
  .swoosh {
    position: absolute;
    inset: 0;
    width: 1200px;
    height: 720px;
  }
  .brand-mark {
    position: absolute;
    left: 212px;
    top: 222px;
    width: 280px;
    height: 280px;
    border-radius: 50%;
    background: var(--navy);
  }
  .brand-name {
    position: absolute;
    left: 540px;
    top: 288px;
    color: var(--navy);
    font-family: var(--brand-font);
    font-weight: 400;
    line-height: 1;
  }
  .brand-name__primary {
    display: block;
    font-size: 70px;
    letter-spacing: 2px;
  }
  .brand-name__secondary {
    display: block;
    margin-top: 26px;
    margin-left: 4px;
    font-size: 20px;
    letter-spacing: 43px;
  }
</style>
</head>
<body>
  <main class="card-front">
    <svg class="swoosh" viewBox="0 0 1200 720" aria-hidden="true">
      <path class="swoosh__navy" fill="var(--navy)"
            d="M0,629 Q560,515 1200,602 L1200,613 Q560,532 0,661 Z"/>
      <path class="swoosh__shadow" fill="#d3d8dc"
            d="M0,668 Q560,542 1200,620 L1200,629 Q560,549 0,682 Z"/>
      <path class="swoosh__magenta" fill="var(--magenta)"
            d="M0,682 Q560,549 1200,629 L1200,720 L0,720 Z"/>
    </svg>

    <div class="brand-mark" aria-hidden="true"></div>

    <h1 class="brand-name">
      <span class="brand-name__primary">NIMBUS</span>
      <span class="brand-name__secondary">SYSTEMS</span>
    </h1>
  </main>
</body>
</html>
```